Need a stunning looking Business Card Design for my Telecom Business, Wow FACTOR!

I deal with high level IT Directors , and Contractors.
I need to impress them with a sleek , professional and unique business card.
Im thinking options as far as rounded edges, plastic , or even metal card or die cut on a corner.
Whatever looks better and leave an unforgettable first impression.
im looking for the wow factor.
Front should have the basics info (attached on the picture of current business card)
i would like to add picture of myself somewhere
Back side
should have logo and maybe some pictures or past projects, you can download from my website ( www.lumvexholdings.com)

```html
<!DOCTYPE html>
<html lang="en">
<head>
<meta charset="utf-8">
<title>Lumvex Technologies – Business Card</title>
<link rel="stylesheet" href="https://fonts.googleapis.com/css2?family=Exo+2:wght@400;500;700&display=swap">
<style>
  :root {
    --page: #ffffff;
    --ink: #111418;
    --navy: #1c3a6b;
    --green: #6ad321;
    --blue-light: #5fe3f5;
    --blue-mid: #1fa6d8;
    --blue-dark: #1d4f8f;
    --edge: #2a2a2a;
    --photo-light: #d8d8d8;
    --photo-dark: #7a7a7a;
  }
  * { margin: 0; padding: 0; box-sizing: border-box; }
  html, body { width: 1200px; height: 686px; overflow: hidden; background: var(--page); }
  .card {
    position: relative;
    width: 1200px;
    height: 686px;
    font-family: "Exo 2", sans-serif;
    color: var(--ink);
  }
  .card-shapes { position: absolute; inset: 0; }
  .portrait {
    position: absolute;
    left: 846px; top: 63px;
    width: 206px; height: 206px;
    border-radius: 50%;
    border: 4px solid var(--ink);
    background: radial-gradient(circle at 45% 40%, var(--photo-light), var(--photo-dark));
  }
  .brand {
    position: absolute;
    left: 66px; top: 248px;
    width: 400px;
    text-align: center;
    color: var(--ink);
    font-weight: 500;
  }
  .brand-name { display: block; font-size: 40px; letter-spacing: 2px; line-height: 1; }
  .brand-sub { display: block; font-size: 15px; letter-spacing: 9px; margin-top: 8px; padding-left: 9px; }
  .contact-icon { position: absolute; }
  .phone-list {
    position: absolute;
    left: 151px; top: 358px;
    list-style: none;
    font-size: 27px;
    line-height: 43px;
  }
  .contact-line {
    position: absolute;
    left: 150px;
    font-size: 27px;
    letter-spacing: 0.5px;
  }
  .email { top: 520px; }
  .web { top: 589px; }
  .person {
    position: absolute;
    left: 700px; width: 500px;
    text-align: center;
  }
  .person-name { top: 292px; font-size: 50px; font-weight: 700; letter-spacing: 0.5px; }
  .person-role { top: 362px; font-size: 26px; font-weight: 500; letter-spacing: 0.5px; }
  .person-trade { top: 446px; font-size: 26px; font-weight: 500; }
</style>
</head>
<body>
<main class="card">
  <svg class="card-shapes" width="1200" height="686" viewBox="0 0 1200 686">
    <defs>
      <radialGradient id="panel-glow" cx="700" cy="380" r="600" gradientUnits="userSpaceOnUse">
        <stop offset="0" stop-color="var(--blue-light)"/>
        <stop offset="0.45" stop-color="var(--blue-mid)"/>
        <stop offset="1" stop-color="var(--blue-dark)"/>
      </radialGradient>
      <clipPath id="card-outline">
        <polygon points="50,0 1150,0 1200,50 1200,636 1150,686 50,686 0,636 0,50"/>
      </clipPath>
    </defs>
    <g clip-path="url(#card-outline)">
      <rect width="1200" height="686" fill="#ffffff"/>
      <polygon points="451,0 1200,0 1200,686 851,686" fill="url(#panel-glow)"/>
      <polygon points="419,0 451,0 851,686 823,686" fill="var(--green)"/>
    </g>
    <polygon points="50,1 1150,1 1199,50 1199,636 1150,685 50,685 1,636 1,50" fill="none" stroke="var(--edge)" stroke-width="2"/>
  </svg>

  <div class="portrait" role="img" aria-label="Portrait photo of Ren Takahara"></div>

  <div class="brand">
    <span class="brand-name">LUMVEX</span>
    <span class="brand-sub">TECHNOLOGIES</span>
  </div>

  <svg class="contact-icon" style="left:74px;top:364px" width="48" height="66" viewBox="0 0 48 66">
    <path d="M10 4 C4 6 2 14 4 24 C8 40 18 56 30 62 C36 65 42 62 44 58 L36 46 C34 44 31 45 30 47 L27 50 C20 44 15 34 13 25 L17 23 C19 22 20 20 19 18 L14 5 C13 3 12 3 10 4 Z" fill="var(--green)"/>
  </svg>
  <ul class="phone-list">
    <li>(305) 555-0147 Miami</li>
    <li>(954) 555-0182 Broward</li>
    <li>(561) 555-0129 Palm Beach</li>
  </ul>

  <svg class="contact-icon" style="left:75px;top:518px" width="58" height="40" viewBox="0 0 58 40">
    <rect x="2.5" y="2.5" width="53" height="35" fill="none" stroke="var(--green)" stroke-width="4"/>
    <path d="M3 4 L29 24 L55 4 M3 36 L22 19 M55 36 L36 19" fill="none" stroke="var(--green)" stroke-width="4"/>
  </svg>
  <p class="contact-line email">INFO@LUMVEXHOLDINGS.COM</p>

  <svg class="contact-icon" style="left:77px;top:583px" width="48" height="48" viewBox="0 0 48 48">
    <g fill="none" stroke="var(--green)" stroke-width="3.5">
      <circle cx="24" cy="24" r="21"/>
      <ellipse cx="24" cy="24" rx="9" ry="21"/>
      <path d="M3 24 H45 M7 13 H41 M7 35 H41 M24 3 V45"/>
    </g>
  </svg>
  <p class="contact-line web">WWW.LUMVEXHOLDINGS.COM</p>

  <h1 class="person person-name">Ren Takahara</h1>
  <p class="person person-role">OPERATIONS MANAGER</p>
  <p class="person person-trade">Low Voltage Contractor</p>
</main>
</body>
</html>
```